Industrial Rubber Manufacturer Trade-Show Flyer

We are looking for a flyer to hand out to potential customers while walking the floors of a trade show. I have attached a document coming several of the product lines we currently do. Please refer to our website www.brightvaleflexomers.com for the color we are looking for the gold, brownish, and black colors in our header. I don't have any pictures besides our one of the building. We would like to have rubber extrusion related pictures and / or displays of industries we sell to
Target Market(s)
automotive, rv industry
Industry/Entity Type
Industrial
Font styles to use
Requirements
Must have
- clean look and feel. display information about the company.

```html
<!DOCTYPE html>
<html lang="en">
<head>
<meta charset="utf-8">
<title>Brightvale Flexomers – Trade-Show Flyer</title>
<link href="https://fonts.googleapis.com/css2?family=Source+Sans+3:wght@400;600&family=Cinzel:wght@400;600&display=swap" rel="stylesheet">
<style>
:root{
  --gold:#d8b978;
  --gold-deep:#c9a45e;
  --charcoal:#2f2d29;
  --ink:#333;
  --paper:#fff;
  --backdrop:#e6e4e1;
  --site-tone-a:#8a9a78;
  --site-tone-b:#6d7d55;
  --rubber-a:#4a4a4a;
  --rubber-b:#2c2c2c;
}
*{box-sizing:border-box;margin:0;padding:0}
html,body{width:1056px;height:1200px;overflow:hidden}
body{background:var(--backdrop);font-family:"Source Sans 3",Arial,sans-serif;color:var(--ink);position:relative}
.card{position:absolute;left:103px;width:850px;height:500px;background:var(--paper);box-shadow:0 4px 14px rgba(0,0,0,.25);overflow:hidden}
.card--front{top:62px}
.card--back{top:630px}
.top-rule{position:absolute;left:0;top:0;width:100%;height:18px;background:var(--gold)}
.header{position:absolute;left:0;top:21px;width:100%;height:77px;background:var(--charcoal)}
.brand{position:absolute;left:22px;top:4px;display:flex;align-items:center;gap:14px}
.brand-dot{width:68px;height:68px;border-radius:50%;border:5px solid var(--gold)}
.brand-name{color:#fff;font-size:19px;font-weight:400;letter-spacing:6.5px;line-height:23px;text-transform:uppercase}
.tagline{position:absolute;right:22px;top:19px;font-family:"Cinzel",Georgia,serif;color:#fff;font-size:12px;letter-spacing:5.2px}
.phone{position:absolute;right:18px;top:34px;font-family:"Cinzel",Georgia,serif;color:var(--gold);font-size:26px;letter-spacing:10px}
.footer{position:absolute;left:0;bottom:0;width:100%;height:46px;background:linear-gradient(90deg,#1b1a18,#3a3835 50%,#1b1a18);display:flex;align-items:center;justify-content:space-between;padding:0 26px 0 14px;color:#fff;font-size:16px}
.footer span{display:flex;align-items:center;gap:7px}
.footer svg{flex:none}
/* front */
.site-photo{position:absolute;left:0;top:102px}
.capabilities{position:absolute;left:443px;top:113px;width:384px}
.section-title{color:var(--gold-deep);font-weight:600;font-size:18px;letter-spacing:.3px}
.capabilities p{font-size:13.3px;line-height:16.5px;text-align:justify;margin-top:6px}
.capabilities p.lead-in{text-align:left;margin-top:16px}
.services{position:absolute;left:410px;top:246px;width:440px;height:103px;background:var(--gold);padding:7px 0 0 33px;display:grid;grid-template-columns:148px 1fr;grid-auto-rows:19px;row-gap:4px;color:#fff;font-size:15px;line-height:19px;list-style:none}
.services li,.bullet-list li{display:flex;align-items:center;gap:5px}
.key-products{position:absolute;left:443px;top:361px}
.key-products h3{font-size:14px;font-weight:600;letter-spacing:.3px}
.key-products ul{list-style:none;display:grid;grid-template-columns:149px 1fr;grid-auto-rows:17px;row-gap:3px;margin-top:6px;font-size:13px;line-height:17px}
.key-products li{display:flex;align-items:center;gap:7px}
/* back */
.tab{position:absolute;left:0;width:382px;height:36px;background:var(--charcoal);clip-path:polygon(0 0,370px 0,100% 100%,0 100%);color:var(--gold);font-size:15px;letter-spacing:.4px;padding:9px 0 0 42px}
.tab--materials{top:110px}
.tab--industries{top:304px}
.materials-intro{position:absolute;left:45px;top:152px;font-size:15px}
.bullet-list{position:absolute;left:42px;list-style:none;display:grid;grid-template-columns:187px 1fr;grid-auto-rows:20px;row-gap:3.6px;font-size:15px;line-height:20px}
.bullet-list--materials{top:175px}
.bullet-list--industries{top:350px}
.bullet-list li.indent{padding-left:18px}
.product-photo{position:absolute;left:462px;top:112px;width:385px;height:190px;border-radius:8px;background:linear-gradient(160deg,var(--rubber-a),var(--rubber-b))}
.industry-circles{position:absolute;left:441px;top:318px;display:flex;gap:10px}
.industry-circles div{width:120px;height:120px;border-radius:50%;border:5px solid var(--gold)}
.ic-fuel{background:#6a7088}
.ic-car{background:#b8a27c}
.ic-solar{background:#4a76b0}
</style>
</head>
<body>
<svg width="0" height="0" style="position:absolute">
  <defs>
    <symbol id="chev-dark" viewBox="0 0 12 12"><circle cx="6" cy="6" r="6" fill="#2f2d29"/><path d="M5 3.4 7.6 6 5 8.6" fill="none" stroke="#fff" stroke-width="1.6"/></symbol>
    <symbol id="chev-gold" viewBox="0 0 12 12"><circle cx="6" cy="6" r="6" fill="#d8b978"/><path d="M5 3.4 7.6 6 5 8.6" fill="none" stroke="#fff" stroke-width="1.6"/></symbol>
    <symbol id="tick" viewBox="0 0 10 8"><path d="M1 4 4 7 9 1" fill="none" stroke="#d8b978" stroke-width="1.4"/></symbol>
    <symbol id="pin" viewBox="0 0 12 16"><path d="M6 0a6 6 0 0 0-6 6c0 4.5 6 10 6 10s6-5.5 6-10a6 6 0 0 0-6-6zm0 8.4a2.4 2.4 0 1 1 0-4.8 2.4 2.4 0 0 1 0 4.8z" fill="#d8b978"/></symbol>
    <symbol id="mail" viewBox="0 0 14 10"><rect width="14" height="10" fill="#d8b978"/><path d="M0 0 7 6 14 0" fill="none" stroke="#2f2d29" stroke-width="1.2"/></symbol>
    <symbol id="globe" viewBox="0 0 14 14"><g fill="none" stroke="#d8b978" stroke-width="1.2"><circle cx="7" cy="7" r="6"/><ellipse cx="7" cy="7" rx="2.6" ry="6"/><path d="M1 7h12M2 3.8h10M2 10.2h10"/></g></symbol>
  </defs>
</svg>

<section class="card card--front">
  <div class="top-rule"></div>
  <header class="header">
    <div class="brand"><div class="brand-dot"></div><div class="brand-name">Brightvale<br>Flexomers</div></div>
    <div class="tagline">CUSTOM RUBBER EXTRUSIONS</div>
    <div class="phone">888.555.0147</div>
  </header>

  <svg class="site-photo" width="414" height="352" viewBox="0 0 414 352">
    <defs>
      <linearGradient id="siteTones" x1="0" y1="0" x2="1" y2="1">
        <stop offset="0" stop-color="#8a9a78"/><stop offset="1" stop-color="#6d7d55"/>
      </linearGradient>
    </defs>
    <path role="img" aria-label="Aerial photo of the manufacturing plant and its parking lot" d="M0 0H370Q394 150 402 352H0Z" fill="url(#siteTones)"/>
    <path d="M370 0H381Q408 150 414 352H403Q395 150 370 0Z" fill="#d8b978"/>
  </svg>

  <div class="capabilities">
    <h2 class="section-title">CORE CAPABILITIES:</h2>
    <p>Brightvale Flexomers specializes in the custom design and production of both closed cell sponge and solid rubber &amp; plastic extrusions. Our use of a continuous cure process provides any length of extrusion required. Industry leader in tape applications.</p>
    <p class="lead-in">Complete In-house tooling and finishing capabilities including:</p>
  </div>

  <ul class="services">
    <li><svg width="11" height="11"><use href="#chev-dark"/></svg>Tool &amp; Die Shop</li>
    <li><svg width="11" height="11"><use href="#chev-dark"/></svg>Notching</li>
    <li><svg width="11" height="11"><use href="#chev-dark"/></svg>Cutting</li>
    <li><svg width="11" height="11"><use href="#chev-dark"/></svg>Retail Packaging</li>
    <li><svg width="11" height="11"><use href="#chev-dark"/></svg>Taping</li>
    <li><svg width="11" height="11"><use href="#chev-dark"/></svg>Vulcanized Splicing</li>
    <li><svg width="11" height="11"><use href="#chev-dark"/></svg>Hole punch</li>
    <li><svg width="11" height="11"><use href="#chev-dark"/></svg>Flocking</li>
  </ul>

  <div class="key-products">
    <h3>KEY PRODUCTS</h3>
    <ul>
      <li><svg width="10" height="8"><use href="#tick"/></svg>RV Sealing Products</li>
      <li><svg width="10" height="8"><use href="#tick"/></svg>Protector Sleeves</li>
      <li><svg width="10" height="8"><use href="#tick"/></svg>Gaskets &amp; Seals</li>
      <li><svg width="10" height="8"><use href="#tick"/></svg>Anti-Vibration Pads</li>
      <li><svg width="10" height="8"><use href="#tick"/></svg>Tubes</li>
      <li><svg width="10" height="8"><use href="#tick"/></svg>Weather-Stripping</li>
    </ul>
  </div>

  <footer class="footer">
    <span><svg width="12" height="16"><use href="#pin"/></svg>4410 County Road 12 Millbrook, OH 44021</span>
    <span><svg width="14" height="10"><use href="#mail"/></svg>info@brightvaleflexomers.com</span>
    <span><svg width="14" height="14"><use href="#globe"/></svg>brightvaleflexomers.com</span>
  </footer>
</section>

<section class="card card--back">
  <div class="top-rule"></div>
  <header class="header">
    <div class="brand"><div class="brand-dot"></div><div class="brand-name">Brightvale<br>Flexomers</div></div>
    <div class="tagline">CUSTOM RUBBER EXTRUSIONS</div>
    <div class="phone">888.555.0147</div>
  </header>

  <div class="tab tab--materials">MATERIAL SPECIALTY</div>
  <p class="materials-intro">Industry leader in sponge application</p>
  <ul class="bullet-list bullet-list--materials">
    <li><svg width="11" height="11"><use href="#chev-gold"/></svg>EPDM</li>
    <li><svg width="11" height="11"><use href="#chev-gold"/></svg>SBR</li>
    <li class="indent">(Dense / Sponge)</li>
    <li><svg width="11" height="11"><use href="#chev-gold"/></svg>Polyisoprene</li>
    <li><svg width="11" height="11"><use href="#chev-gold"/></svg>Silicone</li>
    <li><svg width="11" height="11"><use href="#chev-gold"/></svg>Dual Duro</li>
    <li><svg width="11" height="11"><use href="#chev-gold"/></svg>Nitrile</li>
    <li><svg width="11" height="11"><use href="#chev-gold"/></svg>TPV / TPE / TPV</li>
    <li><svg width="11" height="11"><use href="#chev-gold"/></svg>Neoprene</li>
    <li><svg width="11" height="11"><use href="#chev-gold"/></svg>PVC (Flexible)</li>
  </ul>

  <div class="tab tab--industries">INDUSTRIES SERVER</div>
  <ul class="bullet-list bullet-list--industries">
    <li><svg width="11" height="11"><use href="#chev-gold"/></svg>Recreational Vehicles</li>
    <li><svg width="11" height="11"><use href="#chev-gold"/></svg>Agriculture</li>
    <li><svg width="11" height="11"><use href="#chev-gold"/></svg>Industrial</li>
    <li><svg width="11" height="11"><use href="#chev-gold"/></svg>Heavy Equipment</li>
    <li><svg width="11" height="11"><use href="#chev-gold"/></svg>Automotive</li>
    <li><svg width="11" height="11"><use href="#chev-gold"/></svg>Electrical &amp; Lighting</li>
    <li><svg width="11" height="11"><use href="#chev-gold"/></svg>Window &amp; Door</li>
  </ul>

  <div class="product-photo" role="img" aria-label="Bundle of black rubber extrusion profiles and tubes"></div>

  <div class="industry-circles">
    <div class="ic-fuel" role="img" aria-label="Photo of a fuel station"></div>
    <div class="ic-car" role="img" aria-label="Photo of a classic car"></div>
    <div class="ic-solar" role="img" aria-label="Photo of solar panels"></div>
  </div>

  <footer class="footer">
    <span><svg width="12" height="16"><use href="#pin"/></svg>4410 County Road 12 Millbrook, OH 44021</span>
    <span><svg width="14" height="10"><use href="#mail"/></svg>info@brightvaleflexomers.com</span>
    <span><svg width="14" height="14"><use href="#globe"/></svg>brightvaleflexomers.com</span>
  </footer>
</section>
</body>
</html>
```